TV Media buying firm needs Lead Gen page layout

We need a landing page using our current website look and feel to capture leads from our Pixelnest ads. A quick form to capture Name, phone number, email, and a short message.
The call to action button should state "Get a free direct response campaign audit now!"
Updates

please visit www.brantwellmedia.com for the look and feel of the landing page.

I also uploaded a screenshot of what kind of landing page we are looking for.
the image has been reduced to 50% for the overall view.
thanks!

Please use our website's look and feel as reference for colors, fonts,header and footers.

The video placement on the sample file can be an image or combination image & text.

Again, please reference www.brantwellmedia.com for the look and feel.

Target Market(s)

50+ Market, Cheif Marketing Officer, Summit 1000 Companies

Industry/Entity Type

Tv

```html
<!DOCTYPE html>
<html lang="en">
<head>
<meta charset="utf-8">
<title>Brantwell Media – Free Marketing Audit</title>
<link href="https://fonts.googleapis.com/css2?family=Arimo:ital,wght@0,400;0,700;1,700&family=Caveat:wght@400&display=swap" rel="stylesheet">
<style>
:root{
  --canvas:#e9e9e9;
  --page:#efefef;
  --ink:#1c1c1c;
  --muted:#555;
  --red:#d7141a;
  --red-dark:#a51d1d;
  --bar:#2a2a2a;
  --white:#fff;
  --field-border:#d5d5d5;
  --form-bg:#e6e6e6;
  --icon-grey:#9a9a9a;
  --yellow:#f7c21a;
  --yellow-dark:#f0a400;
  --green:#21a51f;
  --green-dark:#158a14;
  --logo-grey:#3a3a3a;
}
*{box-sizing:border-box;margin:0;padding:0}
html,body{width:1200px;height:1000px;overflow:hidden}
body{background:var(--canvas);font-family:"Arimo",Arial,sans-serif;color:var(--ink)}
.page{position:absolute;left:124px;top:0;width:952px;height:1000px;
  background:linear-gradient(160deg,#f6f6f6 0%,#e8e8e8 45%,#f2f2f2 100%);overflow:hidden}
.topbar{height:21px;background:repeating-linear-gradient(45deg,#2c2c2c 0 2px,#3a3a3a 2px 4px);
  color:var(--white);font-size:9px;display:flex;align-items:center;justify-content:space-between;padding:0 108px 0 90px}
.topbar .call{font-weight:700}
.topbar .call::before{content:"";display:inline-block;width:6px;height:6px;border-radius:50%;background:var(--red);margin-right:5px}
.brand{position:absolute;left:88px;top:32px;display:flex;align-items:center;gap:8px}
.brand-mark{width:14px;height:14px;background:var(--red)}
.brand-name{font-size:28px;font-weight:700;color:var(--ink);letter-spacing:-0.5px}
.headline{position:absolute;left:88px;top:100px;font-size:25px;font-weight:700;line-height:31px}
.headline em{color:var(--red);font-size:29px}
.video{position:absolute;left:88px;top:178px;width:369px;height:228px;border-radius:3px;overflow:hidden;box-shadow:0 2px 6px rgba(0,0,0,.35)}
.video-still{height:206px;background:radial-gradient(ellipse at 45% 40%,#eef1f8 0%,#b9c0d8 60%,#8e97b8 100%)}
.video-controls{height:22px;background:linear-gradient(#2a2a2a,#111);display:flex;align-items:center;gap:10px;padding:0 10px;color:#ddd;font-size:9px}
.video-controls .progress{width:40px;height:3px;background:var(--red)}
.video-controls .spacer{flex:1}
.report-note{position:absolute;left:486px;top:152px;font-family:"Caveat",cursive;font-size:17px;line-height:17px;color:#333}
.report-arrow{position:absolute;left:485px;top:200px}
.lead-form{position:absolute;left:591px;top:86px;width:283px;height:364px;background:var(--white);box-shadow:0 1px 4px rgba(0,0,0,.2)}
.lead-form h2{height:52px;background:linear-gradient(var(--red),#b50f14);color:var(--white);font-size:14px;line-height:16px;text-align:center;padding-top:10px;font-weight:700}
.form-panel{margin:8px 12px 0;background:var(--form-bg);padding:10px 12px 10px;height:290px}
.field{display:flex;align-items:center;gap:9px;margin-bottom:14px}
.field-icon{width:27px;height:27px;border-radius:50%;background:var(--icon-grey);display:flex;align-items:center;justify-content:center}
.field-input{flex:1;height:26px;background:var(--white);border:1px solid var(--field-border);font-size:11px;color:#888;padding:6px 8px}
.field-input b{color:var(--red);font-weight:400}
.cta{display:block;margin:16px auto 0;width:234px;height:45px;border-radius:23px;background:linear-gradient(var(--yellow),var(--yellow-dark));
  border:1px solid #d99400;font:700 12px "Arimo",Arial,sans-serif;color:#333}
.privacy{font-size:8px;color:var(--muted);text-align:center;margin-top:9px}
.client-strip{position:absolute;left:0;top:491px;width:100%;height:71px;border-top:3px solid var(--red);
  background:linear-gradient(#fafafa,#ececec);display:flex;align-items:center;justify-content:center;gap:34px}
.client{font-size:22px;font-weight:700;color:var(--logo-grey)}
.content{position:absolute;left:42px;top:583px;width:898px;height:360px;background:var(--white);border:1px solid #ddd;border-radius:3px}
.feature{position:absolute;width:250px}
.feature-icon{position:absolute;left:-54px;top:-4px}
.feature h3{font-size:14px;font-weight:400;padding-bottom:6px;border-bottom:1px dashed #999;margin-bottom:8px}
.feature ul{list-style:none}
.feature li{font-size:11px;color:#555;line-height:14px;margin-bottom:9px;padding-left:14px;position:relative}
.feature li::before{content:"";position:absolute;left:0;top:5px;width:4px;height:4px;background:var(--red)}
.testimonial{position:absolute;left:606px;top:20px;width:255px}
.avatar{position:absolute;left:-2px;top:0;width:44px;height:44px;border-radius:50%;border:2px solid #ddd;background:radial-gradient(circle at 50% 40%,#f3d7c5,#b07b5a)}
.testimonial h3{margin-left:56px;font-size:14px;font-style:italic;font-weight:700;padding:6px 0 6px;border-bottom:1px dashed #999}
.quote{margin-left:56px;font-size:11px;line-height:14px;color:#444;margin-top:10px}
.quote p{margin-bottom:6px}
.quote .author{font-weight:700;color:var(--ink);margin-top:8px}
.learn-more{position:absolute;left:644px;top:192px;width:222px;text-align:center}
.learn-more p{font-size:12px;font-weight:700;padding-bottom:8px;border-bottom:1px solid #ccc}
.visit{display:block;margin:16px auto 0;width:120px;height:39px;background:linear-gradient(#2fbd2c,var(--green-dark));color:var(--white);
  font:700 12px "Arimo",Arial,sans-serif;border:1px solid var(--green-dark)}
.footer{position:absolute;left:0;top:955px;width:100%;font-size:9px;display:flex;padding:0 90px 0 72px}
.footer .copy{flex:1}
.footer nav{display:flex;gap:26px}
</style>
</head>
<body>
<main class="page">
  <header class="topbar">
    <span>DRTV, Media Buying, Direct Response Television, DRTV Advertising, World Class Media Buying Agency - Brantwell Media</span>
    <span class="call">Call Us: 555-014-2290</span>
  </header>

  <div class="brand"><span class="brand-mark"></span><span class="brand-name">brantwellmedia</span></div>

  <h1 class="headline">Are Your Marketing Campaings<br>Been <em>Efficient?</em></h1>

  <figure class="video">
    <div class="video-still" role="img" aria-label="Video still titled What is Direct Response Television"></div>
    <div class="video-controls">
      <svg width="10" height="10" viewBox="0 0 10 10"><path d="M1 0 L9 5 L1 10Z" fill="#ddd"/></svg>
      <svg width="12" height="10" viewBox="0 0 12 10"><path d="M0 3h3l4-3v10L3 7H0z" fill="#ddd"/></svg>
      <span class="progress"></span>
      <span>0:00 / 3:34</span>
      <span class="spacer"></span>
      <svg width="10" height="10" viewBox="0 0 10 10"><path d="M0 0h4M0 0v4M10 0H6M10 0v4M0 10h4M0 10V6M10 10H6M10 10V6" stroke="#ddd" stroke-width="1.5"/></svg>
    </div>
  </figure>

  <p class="report-note">Get Your FREE<br>Report, Now!</p>
  <svg class="report-arrow" width="95" height="30" viewBox="0 0 95 30">
    <path d="M4 18 C10 32 50 26 90 10" fill="none" stroke="#333" stroke-width="1.6"/>
    <path d="M82 6 L91 10 L84 17" fill="none" stroke="#333" stroke-width="1.6"/>
  </svg>

  <form class="lead-form">
    <h2>DISCOVER if You'r Wasting Money<br>On Your Marketing Camapaings!</h2>
    <div class="form-panel">
      <div class="field"><span class="field-icon"><svg width="12" height="12" viewBox="0 0 12 12"><circle cx="6" cy="4" r="2.6" fill="none" stroke="#fff" stroke-width="1.2"/><path d="M1 12c0-3 2.5-4.5 5-4.5s5 1.5 5 4.5" fill="none" stroke="#fff" stroke-width="1.2"/></svg></span><span class="field-input">Name <b>*</b></span></div>
      <div class="field"><span class="field-icon"><svg width="12" height="10" viewBox="0 0 12 10"><rect x=".6" y=".6" width="10.8" height="8.8" fill="none" stroke="#fff" stroke-width="1.2"/><path d="M1 1l5 4 5-4" fill="none" stroke="#fff" stroke-width="1.2"/></svg></span><span class="field-input">Email <b>*</b></span></div>
      <div class="field"><span class="field-icon"><svg width="8" height="13" viewBox="0 0 8 13"><rect x=".6" y=".6" width="6.8" height="11.8" rx="1" fill="none" stroke="#fff" stroke-width="1.2"/></svg></span><span class="field-input">Phone <b>*</b></span></div>
      <div class="field"><span class="field-icon"><svg width="12" height="12" viewBox="0 0 12 12"><path d="M5 7l2-2M4 6L2 8a2 2 0 0 0 2 2l2-2M8 6l2-2a2 2 0 0 0-2-2L6 4" fill="none" stroke="#fff" stroke-width="1.2"/></svg></span><span class="field-input">Web site Url <b>*</b></span></div>
      <div class="field"><span class="field-icon"><svg width="12" height="12" viewBox="0 0 12 12"><rect x=".6" y="2" width="9" height="9.4" fill="none" stroke="#fff" stroke-width="1.2"/><path d="M5 7l6-6" stroke="#fff" stroke-width="1.2"/></svg></span><span class="field-input">Message <b>*</b></span></div>
      <button class="cta" type="button">Get A Free Online Marketing Audit!</button>
      <p class="privacy">We will NOT share your email or Spam you!</p>
    </div>
  </form>

  <section class="client-strip" aria-label="Clients">
    <span class="client">Orbitview</span>
    <span class="client">MedPoint</span>
    <span class="client">IronCraft</span>
    <span class="client">TaxNimbus</span>
    <span class="client">Wallmark</span>
  </section>

  <section class="content">
    <article class="feature" style="left:69px;top:27px">
      <svg class="feature-icon" width="38" height="34" viewBox="0 0 38 34"><path d="M10 1h18l9 16-9 16H10L1 17z" fill="var(--red-dark)"/><path d="M13 14h4l6-4v14l-6-4h-4z" fill="none" stroke="#fff" stroke-width="1.4"/></svg>
      <h3>Dummy Title Text Example</h3>
      <ul><li>Improve your comapny's online brand exposure.</li><li>Build your website organic search en-gine ranking</li><li>Improve your comapny's online brand exposure.</li></ul>
    </article>
    <article class="feature" style="left:366px;top:29px">
      <svg class="feature-icon" width="38" height="34" viewBox="0 0 38 34"><path d="M10 1h18l9 16-9 16H10L1 17z" fill="var(--red-dark)"/><rect x="12" y="10" width="14" height="14" fill="none" stroke="#fff" stroke-width="1.4"/><path d="M14 21l4-4 3 2 4-5" fill="none" stroke="#fff" stroke-width="1.4"/></svg>
      <h3>Dummy Title Text Example</h3>
      <ul><li>Improve your comapny's online brand exposure.</li><li>Build your website organic search en-gine ranking</li><li>Improve your comapny's online brand exposure.</li></ul>
    </article>
    <article class="feature" style="left:69px;top:188px">
      <svg class="feature-icon" width="38" height="34" viewBox="0 0 38 34"><path d="M10 1h18l9 16-9 16H10L1 17z" fill="var(--red-dark)"/><circle cx="19" cy="17" r="2" fill="#fff"/><ellipse cx="19" cy="17" rx="7" ry="3" fill="none" stroke="#fff" stroke-width="1.2"/><ellipse cx="19" cy="17" rx="3" ry="7" fill="none" stroke="#fff" stroke-width="1.2"/></svg>
      <h3>Dummy Title Text Example</h3>
      <ul><li>Improve your comapny's online brand exposure.</li><li>Build your website organic search en-gine ranking</li><li>Improve your comapny's online brand exposure.</li></ul>
    </article>
    <article class="feature" style="left:366px;top:191px">
      <svg class="feature-icon" width="38" height="34" viewBox="0 0 38 34"><path d="M10 1h18l9 16-9 16H10L1 17z" fill="var(--red-dark)"/><rect x="11" y="11" width="16" height="11" fill="none" stroke="#fff" stroke-width="1.4"/><path d="M16 25h6" stroke="#fff" stroke-width="1.4"/></svg>
      <h3>Dummy Title Text Example</h3>
      <ul><li>Improve your comapny's online brand exposure.</li><li>Build your website organic search en-gine ranking</li><li>Improve your comapny's online brand exposure.</li></ul>
    </article>

    <aside class="testimonial">
      <div class="avatar" role="img" aria-label="Portrait photo of the client giving the testimonial"></div>
      <h3>Testimonial</h3>
      <div class="quote">
        <p>"Lorem ipsum dolor sit amet, consectetu adipisicing elit, sed do eiusmod tempor incididunt ut labore et dolore magna alil.</p>
        <p>Ut enim ad minim veniam, quis nostrud exercitation ullamco laboris nisi ut aliq uip ex ea commodo consequat"</p>
        <p class="author">CEO Lena P.</p>
      </div>
    </aside>

    <div class="learn-more">
      <p>Do You Want To Learn More...?</p>
      <button class="visit" type="button">Visit Our Site!</button>
    </div>
  </section>

  <footer class="footer">
    <span class="copy">© Brantwell Media</span>
    <nav><span>Privacy Police</span><span>Terms and Conditions</span><span>Get Stardeted!</span><span>Pricing</span><span>Contact Us</span></nav>
  </footer>
</main>
</body>
</html>
```